Book Cover for Lanterns Beyond the Quiet Tide

I need a book cover for a 6 x 9 paperback titled Lanterns Beyond the Quiet Tide Told by Scholars and Souls Dwelling in the Realm past Our Realm. It has to do with consciousness, the mind, incarnation onto Earth, leaving Earth, and the life in the life after this life. I have an idea I'm providing with this description, but I am open to anything that would be striking and stimulating, whether with a book or not. I am the author, T. Dwight Falmer. I've added another background idea to see if anyone can do something with it and I've increased the budget.

```html
<!DOCTYPE html>
<html lang="en">
<head>
<meta charset="utf-8">
<title>Lanterns Beyond the Quiet Tide — T. Dwight Falmer</title>
<link rel="stylesheet" href="https://fonts.googleapis.com/css2?family=Cinzel:wght@400&family=Domine:wght@400&family=Cormorant+Garamond:wght@500&display=swap">
<style>
  :root {
    --page: #ffffff;
    --cover: #070405;
    --title-gold: #e2cbab;
    --ink-light: #f6f1ea;
    --glow-core: #fff6e6;
    --glow-warm: #b79466;
    --glow-deep: #3a2a1c;
  }
  html, body {
    margin: 0;
    padding: 0;
    width: 800px;
    height: 1200px;
    overflow: hidden;
    background: var(--page);
  }
  .cover {
    position: absolute;
    left: 30px;
    top: 44px;
    width: 740px;
    height: 1111px;
    background: var(--cover);
    box-shadow: 0 0 8px rgba(0,0,0,0.55);
    overflow: hidden;
  }
  .title {
    position: absolute;
    left: 0;
    top: 80px;
    width: 100%;
    margin: 0;
    text-align: center;
    font-family: "Cinzel", "Trajan Pro", serif;
    font-weight: 400;
    font-size: 118px;
    line-height: 1;
    letter-spacing: 1px;
    color: var(--title-gold);
  }
  .title-rule {
    position: absolute;
    left: 132px;
    top: 224px;
    width: 479px;
    height: 3px;
    background: var(--ink-light);
  }
  .subtitle {
    position: absolute;
    left: 0;
    top: 247px;
    width: 100%;
    margin: 0;
    text-align: center;
    font-family: "Domine", Georgia, serif;
    font-weight: 400;
    font-size: 31px;
    line-height: 50px;
    color: var(--ink-light);
  }
  .subtitle span { display: block; }
  .cover-art {
    position: absolute;
    left: 40px;
    top: 400px;
    width: 660px;
    height: 570px;
    background:
      radial-gradient(ellipse 28% 30% at 50% 70%, var(--glow-core) 0%, rgba(255,246,230,0) 100%),
      radial-gradient(ellipse 50% 55% at 50% 62%, rgba(183,148,102,0.75) 0%, rgba(58,42,28,0.45) 55%, rgba(7,4,5,0) 100%);
  }
  .author {
    position: absolute;
    left: 0;
    top: 1000px;
    width: 100%;
    margin: 0;
    text-align: center;
    font-family: "Cormorant Garamond", Garamond, serif;
    font-weight: 500;
    font-size: 70px;
    line-height: 1;
    color: var(--ink-light);
  }
</style>
</head>
<body>
  <main class="cover">
    <h1 class="title">LANTERNS</h1>
    <div class="title-rule"></div>
    <p class="subtitle">
      <span>Beyond the Quiet Tide</span>
      <span>Told by Scholars and Souls Dwelling</span>
      <span>in the Realm past Our Realm</span>
    </p>
    <div class="cover-art" role="img" aria-label="An open book with fanned pages glowing with warm golden light, surrounded by drifting sparkles and stars against the dark"></div>
    <p class="author">T. Dwight Falmer</p>
  </main>
</body>
</html>
```